Elder abuse Infographic Poster for doctor surgeries

I am looking for someone to redesign, or clean up an infographic poster that we have drafted to raise awareness for Elder abuse. The colour for elder abuse is deep dark purple, and we would like it to be high resolution so it can be printed A3 size and placed in Doctor surgeries. The poster will be used by a not-for-profit in Australia. We are looking to use pictures, rather than heavy text blocks, following the Infographic poster style (I have included a couple of infographic posters for inspiration).
Reason: Providing extra time for more designs :)
Target Market(s)
Older people, 60+
Industry/Entity Type
Doctor
Requirements
Nice to have
- NOTE: You do not need to use the banner etc I have attached, its just an idea for the colours we use etc.
Should not have
- Images of frail older people, pastel colourings, or anything typically associated with frail aged.

```html
<!DOCTYPE html>
<html lang="en">
<head>
<meta charset="utf-8">
<title>No Excuse For Elder Abuse</title>
<link href="https://fonts.googleapis.com/css2?family=Lobster&family=Oswald:wght@500;700&family=Open+Sans:ital,wght@0,400;0,600;0,700;1,400&display=swap" rel="stylesheet">
<style>
  :root{
    --navy:#232f66;
    --blue:#2f7fc1;
    --sky:#dce9f6;
    --paper:#f6f6f9;
    --ink:#2a2d3a;
    --muted:#5b6070;
  }
  *{box-sizing:border-box;margin:0;padding:0}
  html,body{width:826px;height:1200px;overflow:hidden;background:var(--paper)}
  body{font-family:"Open Sans",Arial,sans-serif;color:var(--ink)}
  .poster{position:relative;width:826px;height:1200px;background:#fff;overflow:hidden}
  .abs{position:absolute}

  .title-top{left:0;right:0;top:22px;text-align:center;font-family:"Oswald",sans-serif;font-style:italic;font-weight:700;font-size:48px;line-height:1.2;color:var(--navy);letter-spacing:1px}
  .title-rule{height:4px;background:var(--blue)}
  .title-main{left:0;right:0;top:88px;text-align:center;font-family:"Lobster",cursive;font-size:118px;line-height:1;color:var(--navy)}

  .section-head{display:flex;align-items:center;gap:14px;width:485px;font-family:"Oswald",sans-serif;font-weight:700;font-size:34px;line-height:1.2;color:var(--navy);letter-spacing:.5px;white-space:nowrap}
  .section-head.ruled::after{content:"";flex:1;height:4px;background:var(--blue)}

  .abuse-list{left:40px;top:275px;width:485px;list-style:none}
  .abuse-row{display:flex;align-items:center;height:42px;margin-bottom:6px;border-bottom:3px solid var(--navy)}
  .abuse-type{flex:none;width:210px;height:100%;background:var(--navy);color:#fff;font-family:"Oswald",sans-serif;font-weight:700;font-size:24px;display:flex;align-items:center;padding-left:12px;clip-path:polygon(0 0,100% 0,94% 100%,0 100%)}
  .abuse-desc{padding-left:12px;font-style:italic;font-size:14.5px;color:var(--muted);white-space:nowrap}

  .people{left:560px;top:228px;width:225px;height:252px;border-radius:8px;background:linear-gradient(180deg,#c9dcf0,#e6eef8)}
  .stat{left:560px;top:486px;width:225px}
  .stat-num{font-family:"Oswald",sans-serif;font-weight:700;font-size:40px;line-height:1.2;color:var(--navy);border-bottom:3px solid var(--blue);padding-bottom:2px;display:inline-block}
  .stat-text{font-size:14px;font-style:italic;color:var(--muted);margin-top:6px;line-height:1.3}

  .risk-icons{left:40px;top:625px;width:485px;display:flex;justify-content:space-between}
  .risk{width:110px;text-align:center;font-size:15px;font-weight:600;color:var(--navy);line-height:1.25}
  .risk-art{width:78px;height:78px;border-radius:50%;margin:0 auto 10px;background:linear-gradient(135deg,var(--blue),#6aa6da)}

  .report{left:555px;top:600px;width:235px;height:130px;border:3px dashed var(--navy);border-radius:10px;padding:8px 14px}
  .report-head{font-family:"Oswald",sans-serif;font-weight:700;font-size:28px;line-height:1.3;color:var(--navy)}
  .report-text{font-size:12.5px;font-style:italic;color:var(--muted);width:125px;line-height:1.3;margin-top:2px}
  .police{position:absolute;right:14px;top:50px;width:70px;height:58px;background:var(--navy);border-radius:6px;color:#fff;text-align:center;font-family:"Oswald",sans-serif;font-size:13px;padding-top:8px;line-height:1.2}
  .police b{display:block;font-size:22px}

  .stop-icons{left:40px;top:845px;width:485px;display:flex;justify-content:space-between}
  .stop{width:150px;text-align:center;font-size:16px;font-weight:600;color:var(--navy);line-height:1.25}
  .stop-art{width:80px;height:80px;border-radius:10px;margin:0 auto 10px;background:linear-gradient(135deg,#e9586b,#f28a96)}
  .stop-brand{height:80px;margin-bottom:10px;display:flex;align-items:center;justify-content:center;gap:6px;font-family:"Open Sans",sans-serif;font-weight:700;font-size:24px;color:var(--blue)}
  .stop-brand i{width:14px;height:14px;background:var(--blue);display:block}
  .stop-art.lawyer{background:linear-gradient(135deg,var(--blue),#6aa6da)}

  .helpline{left:40px;top:990px;width:485px;height:130px;background:var(--sky);text-align:center;padding-top:12px}
  .helpline-head{font-family:"Oswald",sans-serif;font-weight:700;font-size:34px;color:var(--navy);line-height:1.1}
  .helpline-num{font-family:"Oswald",sans-serif;font-weight:700;font-size:40px;color:var(--navy);line-height:1.15}
  .helpline-tags{font-style:italic;font-size:14px;color:var(--muted);margin-top:4px}

  .prevention{left:555px;top:745px;width:235px}
  .prevention-head{font-family:"Lobster",cursive;font-size:44px;line-height:1.2;color:var(--navy);text-align:center}
  .prev-list{list-style:none;position:relative;margin-top:8px}
  .prev-list::before{content:"";position:absolute;left:50%;top:0;bottom:0;border-left:3px dashed var(--blue)}
  .prev-item{position:relative;background:#fff;border:3px dashed var(--blue);border-radius:16px;padding:10px 12px;text-align:center;font-style:italic;font-size:14px;color:var(--navy);margin-bottom:24px;line-height:1.3}

  .footer{left:0;right:0;top:1165px;text-align:center;font-style:italic;font-size:14px;color:var(--muted)}
</style>
</head>
<body>
<main class="poster">
  <div class="abs title-rule" style="left:40px;top:52px;width:170px"></div>
  <div class="abs title-rule" style="left:616px;top:52px;width:170px"></div>
  <h1>
    <span class="abs title-top">No Excuse For</span>
    <span class="abs title-main">Elder Abuse</span>
  </h1>
  <div class="abs title-rule" style="left:40px;top:208px;width:746px;height:3px"></div>

  <h2 class="abs section-head" style="left:40px;top:220px">TYPES OF ABUSE</h2>
  <ul class="abs abuse-list">
    <li class="abuse-row"><span class="abuse-type">Psychological</span><span class="abuse-desc">Bullying, shouting, swearing</span></li>
    <li class="abuse-row"><span class="abuse-type">Financial</span><span class="abuse-desc">Taking money, not allowing access</span></li>
    <li class="abuse-row"><span class="abuse-type">Physical</span><span class="abuse-desc">Hitting, slapping, physical harm</span></li>
    <li class="abuse-row"><span class="abuse-type">Neglect</span><span class="abuse-desc">Withholding essential care</span></li>
    <li class="abuse-row"><span class="abuse-type">Sexual</span><span class="abuse-desc">Inappropriate touching, comment</span></li>
    <li class="abuse-row"><span class="abuse-type">Social</span><span class="abuse-desc">Stopping access to family/friends</span></li>
  </ul>

  <div class="abs people" role="img" aria-label="Grid of twenty person icons with one highlighted, showing one in twenty"></div>
  <div class="abs stat">
    <div class="stat-num">1 in 20</div>
    <p class="stat-text">One in twenty older people may experience elder abuse</p>
  </div>

  <h2 class="abs section-head ruled" style="left:40px;top:562px">RISK FACTORS</h2>
  <div class="abs risk-icons">
    <div class="risk"><div class="risk-art" role="img" aria-label="Wheelchair and carer icon"></div>Dependence on Others</div>
    <div class="risk"><div class="risk-art" role="img" aria-label="Heart with pulse icon"></div>Health Issues</div>
    <div class="risk"><div class="risk-art" role="img" aria-label="Person in bed icon"></div>Isolation</div>
    <div class="risk"><div class="risk-art" role="img" aria-label="Piggy bank icon"></div>Difficulty Managing Money</div>
  </div>

  <section class="abs report">
    <div class="report-head">REPORT IT!</div>
    <p class="report-text">Elder abuse is often a crime. If you are in danger, contact the police.</p>
    <div class="police">POLICE<b>000</b></div>
  </section>

  <h2 class="abs section-head ruled" style="left:40px;top:785px">STOPPING ABUSE</h2>
  <div class="abs stop-icons">
    <div class="stop"><div class="stop-art" role="img" aria-label="Health provider icon"></div>Speak to your Health Provider</div>
    <div class="stop"><div class="stop-brand"><i></i>Carewell</div>Contact an Advocate</div>
    <div class="stop"><div class="stop-art lawyer" role="img" aria-label="Handshake icon"></div>Consult a Lawyer</div>
  </div>

  <section class="abs helpline">
    <div class="helpline-head">ELDER ABUSE HELPLINE</div>
    <div class="helpline-num">1300 555 018</div>
    <p class="helpline-tags">Free · Confidential · Client Focused · Independent</p>
  </section>

  <section class="abs prevention">
    <h2 class="prevention-head">Prevention</h2>
    <ul class="prev-list">
      <li class="prev-item">Stay connected to friends, family, and community</li>
      <li class="prev-item">Access professional services to prevent dependence</li>
      <li class="prev-item">Know your rights</li>
      <li class="prev-item" style="margin-bottom:0">Consult a lawyer before signing any agreements</li>
    </ul>
  </section>

  <p class="abs footer">This poster produced by Carewell Inc. (08) 5550 2741</p>
</main>
</body>
</html>
```